Quillbrook Health needs a new services brochure

We need a new brochure that highlights the services that we offer at our clinic. We are a multidisciplinary health clinic that focuses on injury rehabilitation and pain management. We are looking for a brochure that will highlight our primary services to our clientele and inform potential clients of what we can offer. We pride ourselves on our quality of care and our advanced treatment techniques.
Target Market(s)
young families, athletes, people interested in their health.
Industry/Entity Type
Health And Wellness
Colors
Designer to choose colors to be used in the design.
Requirements
Must have
- We would love our new brochure to be a tri-fold that has 6 pages. We would like it to have brief information about our featured services:
- - Chiropractic
- - Massage Therapy
- - Manual Osteopathic Therapy
- - Acupuncture
- - Laser Therapy
- - Radial Shockwave Therapy
- We would also like this brochure to include a brief price list and direct billing info, About Us section & Contact information.
Nice to have
- If there is space to list that we also offer other services such as : Tissue Unwind Method, Hot Stone Massage, Cupping Technique, Pembrill Method, and Kinesiology Taping that would be great. We would like to use images similar to those that are on our website (we have hi-res of all images on the website) www.quillbrookhealth.ca and colours that would fit with our logo.

```html
<!DOCTYPE html>
<html lang="en">
<head>
<meta charset="utf-8">
<title>Quillbrook Health – Services Brochure</title>
<link href="https://fonts.googleapis.com/css2?family=Raleway:wght@400;500;600;700&family=Open+Sans:ital,wght@0,400;0,600;1,800&display=swap" rel="stylesheet">
<style>
:root{
  --blue:#1f7fd8;
  --blue-deep:#1769bd;
  --blue-pale:#d9eaf8;
  --blue-mist:#eef5fc;
  --heading-grey:#8d9ba7;
  --ink:#1e1e1e;
  --page:#ffffff;
  --backdrop:#e9e6e1;
  --photo-skin:#cfb4a2;
  --photo-dark:#3b4352;
}
*{box-sizing:border-box;margin:0;padding:0}
html,body{width:818px;height:1200px;overflow:hidden;background:var(--backdrop)}
body{position:relative;font-family:"Raleway",Arial,sans-serif;color:var(--ink);font-size:8.4px;line-height:1.27}
.sheet{position:absolute;left:12px;width:792px;height:580px;background:var(--page);overflow:hidden}
.sheet--outside{top:8px}
.sheet--inside{top:600px;height:584px}
.abs{position:absolute}
.photo{position:absolute}
.fold{position:absolute;top:0;bottom:0;width:1px;background:#d7dde3}

.service-title{font-weight:700;font-size:9.6px;letter-spacing:.3px;color:var(--heading-grey);text-transform:uppercase;margin-bottom:2px}
.help-lead{color:#a7b1ba;font-size:8.2px;margin:7px 0 2px}
.ticks{list-style:none}
.ticks li{padding-left:12px;position:relative}
.ticks li::before{content:"";position:absolute;left:2px;top:4px;width:3px;height:3px;border-radius:50%;background:currentColor}
.justify{text-align:justify}

.section-head{font-weight:600;font-size:13px;color:var(--blue);font-variant:small-caps;letter-spacing:.3px;position:relative}
.section-head::after{content:"";position:absolute;left:80px;right:0;top:9px;height:1px;background:var(--blue)}
.section-head::before{content:"";position:absolute;right:-2px;top:7px;width:5px;height:5px;border-radius:50%;background:var(--blue)}

/* other services box */
.other-box{left:8px;top:358px;width:246px;height:220px;background:var(--blue-pale);border-radius:8px;padding:8px 10px}
.other-box .service-title{margin-top:8px;margin-bottom:1px}
.other-box p{font-size:8.3px}

/* prices */
.prices-bar{left:262px;top:160px;width:264px;height:13px;background:var(--blue);color:#fff;font-weight:700;font-size:9px;text-align:center;line-height:13px}
.price-title{font-weight:700;font-size:8.3px;color:var(--blue);text-transform:uppercase;margin-bottom:1px}
.price-table{font-size:7.2px;line-height:1.27;border-collapse:collapse}
.price-table td{padding:0;vertical-align:top}
.price-table td.v{padding-left:4px}
.price-note{font-size:7.2px}

/* footer band */
.contact-band{left:262px;top:528px;width:530px;height:52px;background:var(--blue);border-top:4px solid #9fc8ee;color:#fff}
.address{position:absolute;left:0;width:264px;top:6px;text-align:center;font-size:8.4px;line-height:1.2}
.web{position:absolute;left:264px;width:266px;top:18px;text-align:center;font-size:10.6px;font-weight:500;letter-spacing:.2px}

/* cover */
.brand{left:526px;top:376px;width:266px;text-align:center}
.brand-name{font-family:"Raleway",Arial,sans-serif;font-weight:600;font-size:25px;color:var(--blue-deep);letter-spacing:.3px;display:flex;align-items:center;justify-content:center;gap:7px}
.brand-dot{width:12px;height:12px;border-radius:50%;background:var(--blue);display:inline-block}
.tagline{font-family:"Open Sans",Arial,sans-serif;font-style:italic;font-weight:800;font-size:15.5px;margin-top:6px}
.cover-blurb{font-size:10.4px;line-height:1.28;margin-top:24px;padding:0 12px}

/* inside */
.massage-panel{left:264px;top:0;width:264px;height:584px;background:var(--blue);color:#fff}
.massage-panel .service-title{color:#d2e4f6}
.massage-panel .help-lead{color:#a8cff3}
.body-text{font-size:8.4px}
</style>
</head>
<body>

<!-- OUTSIDE SHEET -->
<section class="sheet sheet--outside" aria-label="Brochure outside: services, prices and cover">
  <svg class="abs" style="left:0;top:0" width="526" height="172" viewBox="0 0 526 172" aria-hidden="true">
    <defs>
      <linearGradient id="band" x1="0" y1="0" x2="1" y2="1">
        <stop offset="0" stop-color="#2a8de2"/><stop offset="1" stop-color="#7cbcf0"/>
      </linearGradient>
    </defs>
    <path d="M0 0H526V150C420 168 330 100 230 130C140 158 60 150 0 170Z" fill="url(#band)"/>
  </svg>
  <div class="photo" role="img" aria-label="Shockwave applicator head on skin" style="left:10px;top:8px;width:140px;height:140px;border-radius:50%;background:radial-gradient(circle at 45% 45%,#cfe6fb,#3f8fd8);border:3px solid #fff"></div>
  <div class="photo" role="img" aria-label="Shockwave treatment on a patient's back" style="left:142px;top:12px;width:132px;height:132px;border-radius:50%;background:radial-gradient(circle at 50% 50%,#e8d4c6,#b99b89);border:3px solid #fff"></div>
  <div class="photo" role="img" aria-label="Laser therapy probe on a patient's arm" style="left:272px;top:24px;width:132px;height:132px;border-radius:50%;background:radial-gradient(circle at 50% 55%,#c9a491,#4a4448);border:3px solid #fff"></div>
  <div class="photo" role="img" aria-label="Glass cupping being applied" style="left:400px;top:20px;width:132px;height:132px;border-radius:50%;background:radial-gradient(circle at 50% 50%,#f4ece8,#d49b86);border:3px solid #fff"></div>

  <div class="fold" style="left:262px;top:172px"></div>
  <div class="fold" style="left:526px"></div>

  <!-- Shockwave -->
  <div class="abs" style="left:9px;top:168px;width:176px">
    <h2 class="service-title">Calgary Shockwave Therapy</h2>
    <p class="justify">Shockwave Therapy is the latest innovation in the treatment of chronic soft tissue injuries. A projectile is propelled inside the hand-piece where it generates a mechanical pressure wave that is transferred to the human body.</p>
    <p class="help-lead">We can help you with:</p>
    <ul class="ticks">
      <li>Plantar Fasciitis and Heel Spurs</li>
      <li>Patella Tendonitis (runners knee)</li>
      <li>Tennis/ Golfer's Elbow</li>
      <li>Chronic Shoulder Pain</li>
      <li>Neck Pain</li>
      <li>Shin Splints</li>
      <li>Chronic Hip Pain</li>
      <li>Decreased Range of Motion</li>
    </ul>
  </div>
  <div class="photo" role="img" aria-label="Shockwave therapy unit on a wheeled stand" style="left:194px;top:162px;width:62px;height:198px;border-radius:6px 6px 20px 20px;background:linear-gradient(180deg,#dfe6ec,#ffffff 40%,#c8d1d9)"></div>

  <!-- Other services -->
  <div class="abs other-box">
    <h2 class="section-head">Other Services</h2>
    <h3 class="service-title">Tissue Unwind Method,</h3>
    <p class="justify">Hot Stone Massage, decrease muscle tension, increase local circulation increase relaxation decrease stress feel FANSTASTIC!</p>
    <h3 class="service-title">Cupping Technique,</h3>
    <p class="justify">How does it help?, Lifts connective tissue, Loosens adhesions Stretches muscle and connective tissues, Increases local circulation, Increases local lymphatic flow</p>
    <h3 class="service-title">Pembrill Method, and Kinesiology</h3>
    <p>Chronic Muscle Tension, Soft Tissue Fibrosis (rock hard muscles that never seem to loosen up)<br>Scar Tissue<br>Fascial Adhesions<br>Tendonopathies (tennis elbow, golfer elbow)<br>Carpal Tunnel Syndrome</p>
  </div>

  <!-- Prices -->
  <div class="abs prices-bar">PRICES</div>
  <div class="abs" style="left:274px;top:192px;width:130px">
    <h3 class="price-title">Massage Therapy</h3>
    <table class="price-table">
      <tr><td style="width:88px">30 Minute</td><td class="v">$50</td></tr>
      <tr><td>45 Minute</td><td class="v">$75</td></tr>
      <tr><td>60 Minutes</td><td class="v">$90</td></tr>
      <tr><td>90 Minutes</td><td class="v">$130</td></tr>
      <tr><td>Infant Massage Instruction</td><td class="v">$50</td></tr>
    </table>
    <p class="price-note" style="margin-top:9px">Hot Stone Addition<br>+$20 to regular treatment price</p>
    <h3 class="price-title" style="margin-top:9px">Acupuncture</h3>
    <table class="price-table">
      <tr><td style="width:88px">Initial Assessment and<br>Treatment</td><td class="v" style="vertical-align:bottom">$120</td></tr>
      <tr><td>Subsequent Treatment</td><td class="v">$85</td></tr>
    </table>
  </div>
  <div class="abs" style="left:404px;top:192px;width:118px">
    <h3 class="price-title">Laser Therapy</h3>
    <table class="price-table">
      <tr><td style="width:90px">Initial Assessment and<br>Treatment</td><td class="v" style="vertical-align:bottom">$90</td></tr>
      <tr><td>Subsequent Treatments</td><td class="v">$50</td></tr>
    </table>
    <h3 class="price-title" style="margin-top:9px">Shockwave Therapy</h3>
    <table class="price-table">
      <tr><td style="width:90px">Initial Assessment and<br>Treatment</td><td class="v" style="vertical-align:bottom">$90</td></tr>
      <tr><td>Subsequent Treatments</td><td class="v">$75</td></tr>
    </table>
  </div>
  <div class="fold" style="left:270px;top:330px;width:252px;height:1px;bottom:auto;background:#e6eaee"></div>
  <div class="abs" style="left:272px;top:334px;width:250px">
    <h3 class="price-title">Chiropractic</h3>
    <table class="price-table" style="width:224px">
      <tr><td></td><td class="v" style="color:var(--blue);font-weight:700">INITIAL</td><td class="v" style="color:var(--blue);font-weight:700">SUBSEQUENT</td></tr>
      <tr><td>Pediatrics 0-5 yr old</td><td class="v">$115</td><td class="v">$55</td></tr>
      <tr><td>Student ( 6+yrs, full time)</td><td class="v">$115</td><td class="v">$65</td></tr>
      <tr><td>Adult</td><td class="v">$125</td><td class="v">$55</td></tr>
      <tr><td>Senior 65+ yrs</td><td class="v">$115</td><td class="v">$55</td></tr>
      <tr><td>Chiropractic and laser treatment</td><td class="v"></td><td class="v">$95</td></tr>
      <tr><td>Chiropractic and shockwave therapy</td><td class="v"></td><td class="v">$95</td></tr>
    </table>
    <h3 class="price-title" style="margin-top:9px">Manual Osteopathic Therapy</h3>
    <table class="price-table">
      <tr><td style="width:158px">Initial Assessment and Treatment</td><td class="v">$150</td></tr>
      <tr><td>Subsequent Treatment</td><td class="v">$120</td></tr>
    </table>
    <h3 class="price-title" style="margin-top:9px">Pembrill Method</h3>
    <p class="price-note">Included with chiropractic treatment with Dr. Morrow and Dr. Petra and massage therapy with Tom.</p>
    <h3 class="price-title" style="margin-top:9px">Cupping Technique</h3>
    <p class="price-note">Included with massage therapy with Tom and Elise and acupuncture with Dr. Wren</p>
  </div>

  <!-- Cover -->
  <div class="photo" role="img" aria-label="Therapist's hands massaging a patient's back and shoulder" style="left:527px;top:0;width:265px;height:200px;background:linear-gradient(160deg,#2d3a5c,#5a6686 40%,#d9b9a6 75%,#efe3da)"></div>
  <div class="photo" role="img" aria-label="Therapist stretching a patient's leg" style="left:527px;top:200px;width:265px;height:160px;background:linear-gradient(200deg,#f3f1ee,#d8b5a1 60%,#c49c87)"></div>
  <svg class="abs" style="left:527px;top:140px" width="265" height="240" viewBox="0 0 265 240" aria-hidden="true">
    <path d="M0 30C70 80 170 70 265 45V0H265" fill="none"/>
    <path d="M0 40C80 95 180 80 265 55" fill="none" stroke="#fff" stroke-width="8"/>
    <path d="M0 240V190C60 160 130 140 190 100C220 80 245 72 265 70V240Z" fill="#fff"/>
    <path d="M0 185C60 155 130 135 188 96C218 76 244 68 265 65" fill="none" stroke="var(--blue)" stroke-width="6"/>
  </svg>
  <div class="abs brand">
    <div class="brand-name"><span class="brand-dot"></span>Quillbrook Health</div>
    <div class="tagline">Live life pain free</div>
    <p class="cover-blurb">Chiropractic, Massage Therapy, Manual Osteopathy, Acupuncture, Shockwave and Laser Therapy clinic</p>
  </div>

  <div class="abs contact-band">
    <p class="address">Located in: Harrowgate Plaza<br>4415 - 1180 Linden Ridge Way NW<br>Calgary, AB T3P 2K7<br>(403) 555-0148</p>
    <p class="web">www.quillbrookhealth.ca</p>
  </div>
  <div class="abs" style="left:0;top:575px;width:262px;height:5px;background:var(--blue-pale)"></div>
</section>

<!-- INSIDE SHEET -->
<section class="sheet sheet--inside" aria-label="Brochure inside: about us and featured services">
  <!-- Left panel -->
  <div class="photo" role="img" aria-label="Chiropractor adjusting a young child lying on a treatment table" style="left:0;top:0;width:264px;height:254px;background:linear-gradient(150deg,#e8ecef,#cfd6dc 40%,#4a4f5a 65%,#d6c2b4)"></div>
  <svg class="abs" style="left:0;top:220px" width="264" height="40" viewBox="0 0 264 40" aria-hidden="true">
    <path d="M0 28C90 10 180 6 264 14V40H0Z" fill="#fff"/>
  </svg>
  <div class="abs" style="left:22px;top:260px;width:232px">
    <h2 class="section-head">About us</h2>
    <p class="justify body-text" style="margin-top:14px">Quillbrook Health is a Chiropractic, Massage Therapy, Manual Osteopathy, Acupuncture, Shockwave and Laser Therapy clinic. We bring a comprehensive approach to pain relief and injury recovery to help you get back to enjoying a healthy, active life.</p>
    <h2 class="section-head" style="margin-top:20px">Our services</h2>
    <h3 class="service-title" style="margin-top:14px">Calgary Chiropractor</h3>
    <p class="justify body-text">Chiropractic is the assessment, treatment, rehabilitation and prevention of musculoskeletal (bones, muscles, tendons, joints and cartilage) conditions and disorders. Chiropractic care is able to treat these conditions and the effect they have on the nervous system.</p>
    <p class="help-lead">We can help you:</p>
    <ul class="ticks body-text">
      <li>Find relief from pain</li>
      <li>Find relief from headaches</li>
      <li>Improve movement of your back,neck and shoulders</li>
      <li>Improve posture</li>
      <li>Correct foot or gait problems</li>
      <li>Correct or improve TMJ (jaw) dysfunction</li>
      <li>Improve athletic performance</li>
      <li>Increase energy level</li>
    </ul>
  </div>
  <div class="abs" style="left:22px;top:575px;width:94px;height:4px;background:var(--blue-pale)"></div>

  <!-- Middle panel -->
  <div class="abs massage-panel">
    <div class="photo" role="img" aria-label="Hands massaging a patient's upper back" style="left:0;top:0;width:264px;height:170px;background:linear-gradient(180deg,#2f2f33,#6e5a52 45%,#c9a996 80%,#9fc6ea)"></div>
    <div class="abs" style="left:9px;top:172px;width:248px">
      <h3 class="service-title">Calgary Massage Therapy</h3>
      <p class="justify body-text" style="margin-top:8px">Massage Therapy is the assessment and treatment of the soft tissues of the body, specifically, the muscles, connective tissue, tendons, ligaments and joints for the purpose of optimizing health.</p>
      <p class="help-lead">We can help you:</p>
      <ul class="ticks body-text">
        <li>Eliminate pain</li>
        <li>Increase range of motion</li>
        <li>Relax tight muscles</li>
        <li>Decrease headaches</li>
        <li>Correct or improve TMJ (jaw) dysfunction</li>
        <li>Decrease anxiety</li>
        <li>Recover from injuries faster</li>
        <li>Improve posture</li>
        <li>Assist GI function</li>
      </ul>
      <h3 class="service-title" style="margin-top:33px">Calgary Manual Osteopathy</h3>
      <p class="body-text">Manual Osteopathy is the assessment and treatment of all of the components that make up the structure of the human body.</p>
      <p class="help-lead">We can help you find relief from:</p>
      <ul class="ticks body-text">
        <li>Pain</li>
        <li>Joint stiffness</li>
        <li>Sprains</li>
        <li>Plantar Faciitis</li>
        <li>Rotator Cuff injuries</li>
        <li>Whiplash/ MVA injuries</li>
        <li>Back injuries/ pain</li>
        <li>Fibromyalgia</li>
        <li>Headaches</li>
        <li>Muscle injuries</li>
        <li>Ligament tears/ injuries</li>
        <li>Jaw pain/ TMJ disfunction</li>
      </ul>
    </div>
  </div>

  <!-- Right panel -->
  <div class="photo" role="img" aria-label="Therapist's hand working on a patient's bent knee" style="left:528px;top:0;width:264px;height:246px;background:linear-gradient(200deg,#f6f2ef,#e2c6b5 50%,#c59d88)"></div>
  <svg class="abs" style="left:528px;top:216px" width="264" height="40" viewBox="0 0 264 40" aria-hidden="true">
    <path d="M0 20C80 6 180 6 264 18V40H0Z" fill="#fff"/>
  </svg>
  <div class="abs" style="left:547px;top:251px;width:237px">
    <h3 class="service-title">Calgary Acupuncture</h3>
    <p class="justify body-text">Acupuncture is a Traditional Chinese Medicine technique to improve the body's functions and natural healing ability. It works by stimulating specific anatomical sites, commonly referred to as acupuncture points or acupoints.</p>
    <p class="help-lead">We can help you:</p>
    <ul class="ticks body-text">
      <li>Find relief from pain</li>
      <li>Increase energy levels</li>
      <li>Improve overall mood</li>
      <li>Improve bodily functions</li>
      <li>Achieve body homeostasis (internal balance)</li>
    </ul>
    <h3 class="service-title" style="margin-top:22px">Calgary Laser Therapy</h3>
    <p class="justify body-text">Laser Therapy is a non-invasive, painless treatment which uses focused light at specific wavelengths to speed up the healing process and reduce or eliminate pain from injuries and chronic conditions.</p>
    <p class="help-lead">We can help you with:</p>
    <ul class="ticks body-text">
      <li>Post Surgical Incisions</li>
      <li>Wound Healing</li>
      <li>Sprains and Strains</li>
      <li>Arthritis</li>
      <li>Inflammation</li>
      <li>Chronic Pain</li>
      <li>Skin Conditions (psoriasis, cold sores, etc.)</li>
      <li>Shin Splints</li>
      <li>Tendonitis</li>
    </ul>
  </div>
  <div class="photo" role="img" aria-label="Handheld laser therapy probe with blue light" style="left:646px;top:470px;width:128px;height:44px;border-radius:22px;background:linear-gradient(90deg,#3f8be0,#a9d0f5 35%,#f1e3c8 70%,#e8e8e8)"></div>
  <div class="abs" style="left:548px;top:575px;width:112px;height:4px;background:var(--blue-pale)"></div>
</section>

</body>
</html>
```